Heritage Hollow Business Cards

Require a business card design. <br/><br/>Needs to include logo (either round or long version) plus these details:<br/>Maya Torvel<br/>Heritage Hollow<br/>maya@quonbrook.com.au<br/>02 6481 7390<br/>PO Box Glenwarra NSW 2913<br/>www.heritagehollow.com.au<br/><br/>I need in an editable format so that I can create for multiple staff members. <br/><br/>

Target Market(s)

We are an online store selling renovation products to home owners are builders. Looking for a classic classy design.

Industry/Entity Type

Home And Garden

Contact Information for Business Card

Maya Torvel
Heritage Hollow
maya@quonbrook.com.au
02 6481 7390
PO Box Glenwarra NSW 2913
www.heritagehollow.com.au

Colors

Designer to choose colors to be used in the design.

Requirements
Must have
• Must include Logo.

```html
<!DOCTYPE html>
<html lang="en">
<head>
<meta charset="utf-8">
<title>Heritage Hollow Business Cards</title>
<link href="https://fonts.googleapis.com/css2?family=Enriqueta:wght@400&family=Crimson+Text:wght@400&family=Roboto:wght@300;400;500&display=swap" rel="stylesheet">
<style>
  :root {
    --backdrop: #3b3b3d;
    --card-dark: #656567;
    --card-light: #ececec;
    --ink: #2a2a2a;
    --text: #1e1e1e;
    --muted: #4a4a4a;
    --rule: #8a8a8a;
  }
  html, body {
    margin: 0;
    width: 1200px;
    height: 1200px;
    overflow: hidden;
    background: var(--backdrop);
  }
  .canvas {
    position: relative;
    width: 1200px;
    height: 1200px;
  }
  .card {
    position: absolute;
    top: 253px;
    width: 400px;
    height: 691px;
    border-radius: 24px;
  }
  .card--front { left: 152px; background: var(--card-dark); }
  .card--back { left: 653px; background: var(--card-light); }

  .brand {
    position: absolute;
    font-family: "Enriqueta", serif;
    color: var(--ink);
    line-height: 0.95;
    margin: 0;
    font-weight: 400;
  }
  .card--front .brand {
    left: 108px;
    top: 320px;
    font-size: 43px;
  }
  .card--back .brand {
    left: 60px;
    top: 155px;
    font-size: 30px;
  }

  .holder {
    position: absolute;
    left: 48px;
    top: 478px;
    right: 30px;
  }
  .holder__name {
    font-family: "Crimson Text", serif;
    font-size: 31px;
    font-weight: 400;
    color: var(--text);
    margin: 0;
    letter-spacing: -0.3px;
    line-height: 1;
  }
  .holder__rule {
    width: 29px;
    height: 1px;
    background: var(--rule);
    margin: 25px 0 18px;
  }
  .holder__company {
    font-family: "Roboto", sans-serif;
    font-weight: 500;
    font-size: 17px;
    color: var(--text);
    margin: 0 0 7px;
  }
  .contact {
    list-style: none;
    margin: 0;
    padding: 0;
    font-family: "Roboto", sans-serif;
    font-weight: 300;
    font-size: 13.5px;
    color: var(--muted);
  }
  .contact li {
    display: flex;
    align-items: center;
    height: 20px;
  }
  .contact svg {
    width: 11px;
    height: 11px;
    margin-right: 5px;
    flex: none;
  }
  .contact strong { font-weight: 500; }
</style>
</head>
<body>
<main class="canvas">
  <section class="card card--front" aria-label="Card front">
    <p class="brand">Heritage<br>Hollow</p>
  </section>

  <section class="card card--back" aria-label="Card back">
    <p class="brand">Heritage<br>Hollow</p>

    <div class="holder">
      <h1 class="holder__name">MAYA TORVEL</h1>
      <div class="holder__rule"></div>
      <h2 class="holder__company">HERITAGE HOLLOW</h2>
      <ul class="contact">
        <li>
          <svg viewBox="0 0 12 12" aria-hidden="true"><path d="M6 0.5a3.8 3.8 0 0 0-3.8 3.8C2.2 7 6 11.5 6 11.5S9.8 7 9.8 4.3A3.8 3.8 0 0 0 6 0.5zm0 5.3a1.5 1.5 0 1 1 0-3 1.5 1.5 0 0 1 0 3z" fill="#1e1e1e"/></svg>
          PO Box Glenwarra NSW 2913
        </li>
        <li>
          <svg viewBox="0 0 12 12" aria-hidden="true"><path d="M2.4 1l2 2-1 1.3c.6 1.4 1.7 2.5 3.2 3.2l1.2-1 2.1 2-1.2 1.6C5.6 10 2 6.4 1 3.1z" fill="#1e1e1e"/></svg>
          02 6481 7390
        </li>
        <li>
          <svg viewBox="0 0 12 12" aria-hidden="true"><rect x="1" y="2.5" width="10" height="7.5" fill="none" stroke="#1e1e1e" stroke-width="1.3"/><path d="M1 2.8l5 3.8 5-3.8" fill="none" stroke="#1e1e1e" stroke-width="1.2"/></svg>
          maya@quonbrook.com.au
        </li>
        <li>
          <svg viewBox="0 0 12 12" aria-hidden="true"><g fill="none" stroke="#1e1e1e" stroke-width="0.9"><circle cx="6" cy="6" r="5"/><ellipse cx="6" cy="6" rx="2.2" ry="5"/><path d="M1 6h10M1.8 3.5h8.4M1.8 8.5h8.4"/></g></svg>
          www.<strong>heritagehollow</strong>.com.au
        </li>
      </ul>
    </div>
  </section>
</main>
</body>
</html>
```